Design a Website Mockup for Sunlit Orchard

My website is being programmed right now, but I have no design for it. We do have a template ... it is Palquist from BrixLayouts. I need a color scheme, a header layout, a footer layout, and all of the "look and feel" elements. And I need it rather quickly!

I do have a logo already, although the colors on the logo are not set in stone. You can change those if you like.

The concept of the website is a photo scanning service that serves the USA and Canada (mostly the US). As such, I would like it to have a slightly patriotic feel to it. A visitor to the website should feel drawn into the site.

Please ask questions! This is a high priority and I need to get it done.

Added 3-17-2015: I added the wireframes in PPT to this contest.
Dorian

```html
<!DOCTYPE html>
<html lang="en">
<head>
<meta charset="utf-8">
<title>Sunlit Orchard</title>
<link href="https://fonts.googleapis.com/css2?family=Fjalla+One&family=Lato:wght@400;700&display=swap" rel="stylesheet">
<style>
:root{
  --tan:#e0b776;
  --tan-deep:#c9985a;
  --gold:#d9a95e;
  --gold-text:#b98a45;
  --cream:#fde6c0;
  --ink:#2b2e35;
  --hero:#3d4049;
  --white:#ffffff;
  --body:#3a3a3a;
  --muted:#8a8a8a;
}
*{margin:0;padding:0;box-sizing:border-box}
html,body{width:678px;height:1200px;overflow:hidden;background:var(--white)}
body{position:relative;font-family:'Lato',sans-serif;color:var(--body)}
.abs{position:absolute}
.display{font-family:'Fjalla One',sans-serif;text-transform:uppercase}

.header{left:0;top:0;width:678px;height:103px;background:linear-gradient(100deg,#d9ae6c,#e6c389 45%,#dcb173)}
.brand{left:106px;top:16px;width:72px;height:72px;border:1px solid var(--ink);display:flex;align-items:center;justify-content:center;text-align:center;font-size:10px;line-height:1.2;color:var(--ink);text-transform:uppercase}
.search{left:438px;top:41px;width:134px;height:22px;background:var(--white);border:1px solid var(--ink)}
.search-btn{left:555px;top:41px;width:17px;height:22px;background:#111;display:flex;align-items:center;justify-content:center}

.nav{left:0;top:103px;width:678px;height:36px;background:var(--ink);display:flex;align-items:center;justify-content:center;gap:0}
.nav a{color:var(--white);text-decoration:none;font-family:'Fjalla One',sans-serif;font-size:12.5px;text-transform:uppercase;padding:0 11px;border-left:1px solid var(--white);line-height:14px}
.nav a:first-child{border-left:0}

.hero{left:0;top:139px;width:678px;height:290px;background:linear-gradient(90deg,#3a3d46,#4a4b50 55%,#3e4048)}
.hero-title{left:72px;top:205px;width:320px;color:var(--white);font-size:19.5px;line-height:25px}
.hero-text{left:72px;top:276px;width:350px;color:var(--white);font-size:9.5px;line-height:11.5px}
.btn{display:flex;align-items:center;justify-content:center;font-size:10px;text-transform:uppercase;border-radius:3px}
.btn-learn{left:71px;top:335px;width:130px;height:37px;background:var(--ink);color:var(--white);border:1px solid var(--white)}
.btn-hire{left:216px;top:335px;width:130px;height:37px;background:var(--gold);color:var(--white);border:1px solid #f0d3a4}
.hero-photo{left:429px;top:165px;width:192px;height:237px;border:2px solid #e6e6e6;background:linear-gradient(160deg,#f2f2f2,#d9d9d9 60%,#a8a58a)}

.services{left:0;top:429px;width:678px;height:338px;background:var(--cream)}
.services-title{left:0;top:456px;width:678px;text-align:center;color:var(--gold-text);font-size:17px}
.services-sub{left:0;top:479px;width:678px;text-align:center;font-family:'Fjalla One',sans-serif;font-size:8px;color:var(--ink)}
.card{top:520px;width:139px;height:202px;background:var(--white);border:1px solid #eadcc4}
.card-img{width:139px;height:75px}
.card-title{margin-top:14px;text-align:center;font-size:13.5px;color:var(--ink)}
.card-text{margin:6px 10px 0;text-align:center;font-size:6px;line-height:8.2px;color:var(--muted)}
.card-btn{margin:12px auto 0;width:61px;height:20px;background:#3d3f45;color:var(--white);border:1px solid #222;border-radius:3px;font-size:7.5px;display:flex;align-items:center;justify-content:center;text-transform:uppercase}

.about-title{left:0;top:784px;width:678px;text-align:center;color:var(--tan-deep);font-size:21px}
.about-text{left:108px;width:462px;text-align:center;font-size:9.5px;line-height:11.3px;color:var(--body)}

.footer{left:0;top:958px;width:678px;height:183px;background:linear-gradient(120deg,#24262c,#32343a 50%,#3b2f33 80%,#2d2f35)}
.col{top:981px;width:94px}
.col h4{font-weight:400;font-size:11.5px;color:var(--gold);padding-bottom:3px;border-bottom:1px solid #cfcfcf}
.col ul{list-style:none;margin-top:6px}
.col li{font-size:7.8px;font-weight:700;color:var(--white);height:15px;display:flex;align-items:center;gap:5px}
.col li::before{content:"+";color:var(--gold);font-size:9px;font-weight:400}
.footer-brand{left:468px;top:983px;width:102px;height:103px;background:var(--gold);border:1px solid #f3e3c4;outline:1px solid var(--gold);outline-offset:1px;display:flex;align-items:center;justify-content:center;text-align:center;font-size:14px;line-height:1.15;color:var(--ink);text-transform:uppercase}

.bottom{left:0;top:1141px;width:678px;height:59px;background:var(--ink)}
.copy{left:107px;top:1163px;font-size:6.5px;color:#d8d8d8}
.social{left:493px;top:1151px}
</style>
</head>
<body>

<header class="abs header" role="img" aria-label="Warm sepia photo of waving flags under a cloudy sky"></header>
<div class="abs brand">Sunlit<br>Orchard</div>
<div class="abs search"></div>
<div class="abs search-btn">
  <svg width="9" height="9" viewBox="0 0 10 10"><circle cx="6" cy="4" r="3" fill="none" stroke="#fff" stroke-width="1.3"/><line x1="4" y1="6" x2="1" y2="9" stroke="#fff" stroke-width="1.4"/></svg>
</div>

<nav class="abs nav">
  <a>Patriotic Mission</a><a>Products/Services</a><a>Process/Safety/Care</a><a>Pricing</a><a>About Us</a><a>Contact</a>
</nav>

<section class="abs hero" role="img" aria-label="Dimmed background photo of a veteran beside a flag and military vehicle"></section>
<h1 class="abs display hero-title">Lorem ipsum dolor sit amet consectetuer. Aliquam tincidunt mauris eu risus.</h1>
<p class="abs hero-text">Lorem ipsum dolor sit amet, consectetuer adipiscing elit. Donec odio. Quisque volutpat mattis eros. Nullam malesuada erat ut turpis. Suspendisse urna nibh, viverra non,</p>
<div class="abs btn btn-learn">Learn More</div>
<div class="abs btn btn-hire">Hire Our Team</div>
<div class="abs hero-photo" role="img" aria-label="Photo of a soldier in camouflage saluting beside an American flag"></div>

<section class="abs services"></section>
<h2 class="abs display services-title">Lorem ipsum dolor sit amet</h2>
<p class="abs services-sub">Aliquam tincidunt mauris eu risus.</p>

<article class="abs card" style="left:105px">
  <div class="card-img" role="img" aria-label="Photo of a soldier in front of a flag" style="background:linear-gradient(90deg,#b23a48,#e9e4e6 45%,#6e6f74)"></div>
  <h3 class="display card-title">What We Do</h3>
  <p class="card-text">Lorem ipsum dolor sit amet, consectetuer adipiscing elit. Donec odio. Quisque volutpat mattis eros. Nullam malesuada erat ut turpis. Suspendisse urna nibh, viverra non, semper suscipit, posuere a, pede.</p>
  <div class="card-btn">Read More</div>
</article>
<article class="abs card" style="left:270px">
  <div class="card-img" role="img" aria-label="Black and white photo of a memorial sculpture of soldiers" style="background:linear-gradient(135deg,#9a9a9a,#4a4a4a 50%,#7a7a7a)"></div>
  <h3 class="display card-title">What You Get</h3>
  <p class="card-text">Lorem ipsum dolor sit amet, consectetuer adipiscing elit. Donec odio. Quisque volutpat mattis eros. Nullam malesuada erat ut turpis. Suspendisse urna nibh, viverra non, semper suscipit, posuere a, pede.</p>
  <div class="card-btn">Read More</div>
</article>
<article class="abs card" style="left:433px">
  <div class="card-img" role="img" aria-label="Photo of a saluting soldier in a helmet before a flag" style="background:linear-gradient(90deg,#3b4f8c,#8a8a80 50%,#c2484f)"></div>
  <h3 class="display card-title">Why It Matters</h3>
  <p class="card-text">Lorem ipsum dolor sit amet, consectetuer adipiscing elit. Donec odio. Quisque volutpat mattis eros. Nullam malesuada erat ut turpis. Suspendisse urna nibh, viverra non, semper suscipit, posuere a, pede.</p>
  <div class="card-btn">Read More</div>
</article>

<h2 class="abs display about-title">About Us</h2>
<p class="abs about-text" style="top:838px">Lorem ipsum dolor sit amet, consectetuer adipiscing elit. Donec odio. Quisque volutpat mattis eros. Nullam malesuada erat ut turpis. Suspendisse urna nibh, viverra non, semper suscipit, posuere a, pede. Donec nec justo eget felis facilisis fermentum. Aliquam porttitor mauris sit amet orci. Aenean dignissim pellentesque felis.</p>
<p class="abs about-text" style="top:883px">Morbi in sem quis dui placerat ornare. Pellentesque odio nisi, euismod in, pharetra a, ultricies in, diam. Sed arcu. Cras consequat. Praesent dapibus, neque id cursus faucibus, tortor neque egestas augue, eu vulputate magna eros eu erat. Aliquam erat volutpat. Nam dui mi, tincidunt quis, accumsan porttitor, facilisis luctus, metus.</p>

<footer class="abs footer" role="img" aria-label="Dark background of a map overlaid with a faded flag"></footer>
<div class="abs col" style="left:106px">
  <h4>Information</h4>
  <ul><li>Patriotic Mission</li><li>Products/Services</li><li>Process/Safety/Care</li><li>Pricing</li><li>About Us</li><li>Contact</li></ul>
</div>
<div class="abs col" style="left:229px">
  <h4>Customer Service</h4>
  <ul><li>Contact Us</li><li>Returns</li><li>Site Map</li></ul>
</div>
<div class="abs col" style="left:363px">
  <h4>Quick Link</h4>
  <ul><li>Term of US</li><li>Privacy</li><li>Help</li></ul>
</div>
<div class="abs footer-brand">Sunlit<br>Orchard</div>

<div class="abs bottom"></div>
<p class="abs copy">Copyright © - 2015 sunlitorchard.com. All Rights Reserved</p>
<svg class="abs social" width="80" height="40" viewBox="0 0 80 40" aria-label="Social links">
  <circle cx="8" cy="8" r="8" fill="#3b5a9a"/><circle cx="28" cy="8" r="8" fill="#2aa3dc"/><circle cx="48" cy="8" r="8" fill="#2b2e35" stroke="#fff" stroke-width="1"/><circle cx="70" cy="8" r="8" fill="#d9302a"/>
  <circle cx="8" cy="29" r="8" fill="#e8732a"/><circle cx="28" cy="29" r="8" fill="#1a84bc"/><circle cx="48" cy="29" r="8" fill="#c2276b"/><circle cx="70" cy="29" r="8" fill="#c8232c"/>
</svg>

</body>
</html>
```